TLA marine wildlife conservation strategy

The Coastal Habitat Alliance (tla-reefs.org) needs an illustration to explain in a captivating and clear fashion the influences and interactions underlying our marine wildlife conservation planning and policymaking process. This will be included in our forthcoming strategy paper, and widely presented in conferences. Ultimately, this illustration will help governments take the right decisions to protect wildlife and natural resources.
Guidelines:
Size: The illustration shall fit in a A4 page, and also render nicely on a projector screen (1920x1080)
Colors: Avoid too colorful and 'playful' color code
Text: - Case shall be consistent throughout the graphic (unlike the draft design provided)
Graphic elements:
- In the top right of the graphic there is supposed to be a map of Myanmar. The map is attached. Feel free to adjust the map colors and style to match the illustration.
The only key areas we shall include in the map are:
- Myanmar borders
- EEZ (green),
- state/region borders (dotted lines),
- two marine corridors (blue and light red).
Everything else shall be left out (such as minimap, legend, scale, compass, SEZ).
- On the bottom right, it's important for the national benefits to be presented as a Venn diagram like in the original draft illustration (three intersecting circles)
Any questions? Please ask: dmarsh@tla-reefs.org
Thank you!
Target Market(s)
Scientists, policy makers.
Industry/Entity Type
Environment

```html
<!DOCTYPE html>
<html lang="en">
<head>
<meta charset="utf-8">
<title>TLA Marine Spatial Planning Framework</title>
<link rel="stylesheet" href="https://fonts.googleapis.com/css2?family=Open+Sans:wght@400;700;800&family=Courgette&display=swap">
<style>
  :root {
    --canvas: #d9d9d9;
    --margin: #ffffff;
    --box: #b7d8ef;
    --ink: #1a1a1a;
    --green: #99ee77;
    --green-strong: #33c400;
    --orange: #f29c55;
    --orange-strong: #ee8800;
    --blue: #80bfea;
    --blue-strong: #1488e0;
    --script: #1f3fb0;
    --arrow: #8c8c8c;
    --paper: #eeeff1;
    --paper-shade: #c9c9cb;
    --ring-edge: #a0a0a0;
    --venn-econ-social: #e6d775;
    --venn-econ-env: #e070d2;
    --venn-social-env: #c6eaa6;
    --venn-centre: #f1eed8;
  }
  html, body {
    margin: 0;
    padding: 0;
    width: 1200px;
    height: 713px;
    overflow: hidden;
    background: var(--margin);
  }
  .framework {
    display: block;
    width: 1200px;
    height: 713px;
    font-family: "Open Sans", sans-serif;
  }
  .backdrop { fill: var(--canvas); }
  .driver-box { fill: var(--box); }
  .driver-text { font-size: 18px; fill: var(--ink); text-anchor: middle; }
  .gear-label { font-size: 12px; fill: var(--ink); text-anchor: middle; }
  .gear-green { fill: var(--green-strong); }
  .gear-blue { fill: var(--blue-strong); }
  .gear-orange { fill: var(--orange-strong); }
  .teeth { fill: none; stroke-width: 12; stroke-dasharray: 7 6; }
  .teeth-green { stroke: var(--green-strong); }
  .teeth-blue { stroke: var(--blue-strong); }
  .teeth-orange { stroke: var(--orange-strong); }

  .ring-consensus { fill: var(--green); }
  .ring-institutional { fill: var(--blue); }
  .ring-data { fill: var(--orange); }
  .ring-edge { fill: none; stroke: var(--ring-edge); stroke-width: 3; }
  .ring-hole { fill: var(--canvas); }
  .ring-text { font-size: 18px; fill: var(--ink); }

  .band { fill: none; }
  .band-outline-blue { stroke: var(--blue-strong); stroke-width: 34; }
  .band-outline-orange { stroke: var(--orange-strong); stroke-width: 34; }
  .band-outline-green { stroke: var(--green-strong); stroke-width: 34; }
  .band-fill-orange { stroke: var(--orange-strong); stroke-width: 28; }
  .band-fill-green { stroke: var(--green-strong); stroke-width: 28; }
  .band-fill-blue { stroke: var(--blue-strong); stroke-width: 28; }
  .head-orange { fill: var(--orange-strong); stroke: var(--blue-strong); stroke-width: 0.6; }
  .head-green { fill: var(--green-strong); stroke: var(--orange-strong); stroke-width: 0.6; }
  .head-blue { fill: var(--blue-strong); stroke: var(--green-strong); stroke-width: 0.6; }
  .head-grey { fill: var(--arrow); }
  .core-text { font-size: 15px; font-weight: 800; letter-spacing: 1px; fill: var(--ink); }
  .title-script { font-family: "Courgette", cursive; font-size: 44px; fill: var(--script); text-anchor: middle; }

  .flow-arrow { fill: none; stroke: var(--arrow); stroke-width: 10; stroke-linecap: round; }
  .adaptive-text { font-size: 17px; fill: var(--ink); }

  .paper { fill: var(--paper); }
  .paper-shade { fill: var(--paper-shade); }
  .paper-curl { fill: none; stroke: var(--paper-shade); stroke-width: 10; }

  .benefits-script { font-family: "Courgette", cursive; font-size: 38px; fill: var(--script); }
  .venn-economic { fill: var(--orange-strong); }
  .venn-social { fill: var(--green-strong); }
  .venn-environment { fill: var(--blue-strong); }
  .venn-econ-social { fill: var(--venn-econ-social); }
  .venn-econ-env { fill: var(--venn-econ-env); }
  .venn-social-env { fill: var(--venn-social-env); }
  .venn-centre { fill: var(--venn-centre); }
  .venn-label { font-size: 18px; fill: var(--ink); text-anchor: middle; }
</style>
</head>
<body>
<svg class="framework" viewBox="0 0 1262 750" xmlns="http://www.w3.org/2000/svg" aria-labelledby="fw-title">
  <title id="fw-title">Marine spatial planning framework: drivers, process and national benefits</title>
  <defs>
    <marker id="head-orange" viewBox="0 0 10 10" markerUnits="userSpaceOnUse" markerWidth="40" markerHeight="46" refX="1" refY="5" orient="auto">
      <path class="head-orange" d="M0 0 L10 5 L0 10 Z"/>
    </marker>
    <marker id="head-green" viewBox="0 0 10 10" markerUnits="userSpaceOnUse" markerWidth="40" markerHeight="46" refX="1" refY="5" orient="auto">
      <path class="head-green" d="M0 0 L10 5 L0 10 Z"/>
    </marker>
    <marker id="head-blue" viewBox="0 0 10 10" markerUnits="userSpaceOnUse" markerWidth="40" markerHeight="46" refX="1" refY="5" orient="auto">
      <path class="head-blue" d="M0 0 L10 5 L0 10 Z"/>
    </marker>
    <marker id="head-grey" viewBox="0 0 10 10" markerUnits="userSpaceOnUse" markerWidth="28" markerHeight="30" refX="3" refY="5" orient="auto-start-reverse">
      <path class="head-grey" d="M0 0 L10 5 L0 10 L3 5 Z"/>
    </marker>

    <path id="arc-consensus-1" d="M517.5 192.8 A245 245 0 0 1 827.7 247.5"/>
    <path id="arc-consensus-2" d="M518.4 231.4 A212 212 0 0 1 813.6 283.4"/>
    <path id="arc-data" d="M463.9 281.7 A215 215 0 0 0 549.1 599.9"/>
    <path id="arc-dev-1" d="M865.5 322.9 A240 240 0 0 1 598.3 641.4"/>
    <path id="arc-dev-2" d="M828.5 317.1 A208 208 0 0 1 586.2 605.9"/>

    <path id="arc-shared" d="M544.3 324.6 A125 125 0 0 1 728.4 316.6"/>
    <path id="arc-coord" d="M753.3 352.2 A125 125 0 0 1 666 527.3"/>
    <path id="arc-decision" d="M618.3 528.1 A125 125 0 0 1 526.7 352.2"/>

    <clipPath id="clip-econ"><circle cx="1072" cy="528" r="72"/></clipPath>
    <clipPath id="clip-social"><circle cx="1000" cy="648" r="80"/></clipPath>

    <linearGradient id="map-tone" x1="0" y1="0" x2="0" y2="1">
      <stop offset="0" stop-color="#e6d77f"/>
      <stop offset="0.55" stop-color="#e6d77f"/>
      <stop offset="0.56" stop-color="#7fbfe9"/>
      <stop offset="1" stop-color="#7fbfe9"/>
    </linearGradient>
  </defs>

  <rect class="backdrop" x="78" y="0" width="1184" height="750"/>

  <g class="drivers">
    <rect class="driver-box" x="145" y="24" width="210" height="42" rx="4"/>
    <text class="driver-text" x="250" y="52">Political transition</text>

    <rect class="driver-box" x="125" y="98" width="248" height="82" rx="4"/>
    <text class="driver-text" x="250" y="120">Increasing developmental</text>
    <text class="driver-text" x="250" y="144">pressures from rapid</text>
    <text class="driver-text" x="250" y="168">economic growth</text>

    <rect class="driver-box" x="125" y="237" width="236" height="378" rx="4"/>
    <text class="driver-text" x="243" y="262">Weak coordination</text>
    <text class="driver-text" x="243" y="288">between marine sectors</text>

    <rect class="driver-box" x="145" y="650" width="258" height="88" rx="4"/>
    <text class="driver-text" x="274" y="674">Declining</text>
    <text class="driver-text" x="274" y="698">marine and coastal</text>
    <text class="driver-text" x="274" y="722">ecosystems and resources</text>
  </g>

  <g class="sector-gears">
    <g class="gear">
      <circle class="teeth teeth-green" cx="292" cy="334" r="30"/>
      <circle class="gear-green" cx="292" cy="334" r="31"/>
      <text class="gear-label" x="292" y="331">Coastal</text>
      <text class="gear-label" x="292" y="346">tourism</text>
    </g>
    <g class="gear">
      <circle class="teeth teeth-blue" cx="172" cy="380" r="35"/>
      <circle class="gear-blue" cx="172" cy="380" r="36"/>
      <text class="gear-label" x="172" y="366">Marine &amp;</text>
      <text class="gear-label" x="172" y="381">coastal</text>
      <text class="gear-label" x="172" y="396">conservation</text>
    </g>
    <g class="gear">
      <circle class="teeth teeth-orange" cx="262" cy="410" r="40"/>
      <circle class="gear-orange" cx="262" cy="410" r="41"/>
      <text class="gear-label" x="262" y="406">Navy &amp;</text>
      <text class="gear-label" x="262" y="421">marine police</text>
    </g>
    <g class="gear">
      <circle class="teeth teeth-green" cx="180" cy="466" r="40"/>
      <circle class="gear-green" cx="180" cy="466" r="41"/>
      <text class="gear-label" x="180" y="462">Marine</text>
      <text class="gear-label" x="180" y="477">fisheries</text>
    </g>
    <g class="gear">
      <circle class="teeth teeth-blue" cx="272" cy="512" r="46"/>
      <circle class="gear-blue" cx="272" cy="512" r="47"/>
      <text class="gear-label" x="276" y="501">Offshore gas</text>
      <text class="gear-label" x="276" y="516">exploration</text>
      <text class="gear-label" x="276" y="531">&amp; production</text>
    </g>
    <g class="gear">
      <circle class="teeth teeth-orange" cx="212" cy="572" r="30"/>
      <circle class="gear-orange" cx="212" cy="572" r="30"/>
      <text class="gear-label" x="212" y="569">Maritime</text>
      <text class="gear-label" x="212" y="584">transport</text>
    </g>
  </g>

  <g class="driver-arrows">
    <path class="flow-arrow" d="M378 70 Q465 74 492 118" marker-end="url(#head-grey)"/>
    <path class="flow-arrow" d="M382 140 Q414 152 424 184" marker-end="url(#head-grey)"/>
    <path class="flow-arrow" d="M312 460 Q338 468 366 458" marker-end="url(#head-grey)"/>
    <path class="flow-arrow" d="M390 632 Q408 606 426 594" marker-end="url(#head-grey)"/>
  </g>

  <g class="planning-ring">
    <path class="ring-consensus" d="M640 405 L445.5 210.5 A275 275 0 0 1 870.6 255.2 Z"/>
    <path class="ring-institutional" d="M640 405 L870.6 255.2 A275 275 0 0 1 640 680 Z"/>
    <path class="ring-data" d="M640 405 L640 680 A275 275 0 0 1 445.5 210.5 Z"/>
    <circle class="ring-consensus" cx="455" cy="232" r="20"/>
    <circle class="ring-institutional" cx="858" cy="285" r="20"/>
    <circle class="ring-institutional" cx="625" cy="600" r="20"/>
    <circle class="ring-edge" cx="640" cy="405" r="275"/>
    <circle class="ring-hole" cx="640" cy="405" r="152"/>

    <text class="ring-text"><textPath href="#arc-consensus-1" startOffset="50%" text-anchor="middle">Consensus building</textPath></text>
    <text class="ring-text"><textPath href="#arc-consensus-2" startOffset="50%" text-anchor="middle">and capacity development</textPath></text>
    <text class="ring-text"><textPath href="#arc-data" startOffset="50%" text-anchor="middle">Data knowledge strengthening</textPath></text>
    <text class="ring-text"><textPath href="#arc-dev-1" startOffset="35%" text-anchor="middle">Development of</textPath></text>
    <text class="ring-text"><textPath href="#arc-dev-2" startOffset="50%" text-anchor="middle">institutional arrangements</textPath></text>
  </g>

  <g class="core-cycle">
    <path class="band band-outline-blue" d="M544.3 324.6 A125 125 0 0 1 728.4 316.6"/>
    <path class="band band-fill-orange" d="M544.3 324.6 A125 125 0 0 1 728.4 316.6" marker-end="url(#head-orange)"/>
    <path class="band band-outline-orange" d="M753.3 352.2 A125 125 0 0 1 666 527.3"/>
    <path class="band band-fill-green" d="M753.3 352.2 A125 125 0 0 1 666 527.3" marker-end="url(#head-green)"/>
    <path class="band band-outline-green" d="M618.3 528.1 A125 125 0 0 1 526.7 352.2"/>
    <path class="band band-fill-blue" d="M618.3 528.1 A125 125 0 0 1 526.7 352.2" marker-end="url(#head-blue)"/>

    <text class="core-text" dominant-baseline="central"><textPath href="#arc-shared" startOffset="50%" text-anchor="middle">SHARED VISION</textPath></text>
    <text class="core-text" dominant-baseline="central"><textPath href="#arc-coord" startOffset="50%" text-anchor="middle">COORDINATION</textPath></text>
    <text class="core-text" dominant-baseline="central"><textPath href="#arc-decision" startOffset="50%" text-anchor="middle">DECISION SUPPORT</textPath></text>

    <text class="title-script" x="640" y="362">Marine</text>
    <text class="title-script" x="632" y="410">Spatial</text>
    <text class="title-script" x="645" y="460">Planning</text>
  </g>

  <g class="map-scroll">
    <path class="paper" d="M912 70 Q905 30 940 22 L1178 12 Q1170 180 1192 300 L985 362 Q955 368 950 340 Q945 200 912 70 Z"/>
    <ellipse class="paper-shade" cx="926" cy="92" rx="20" ry="24"/>
    <path class="paper-curl" d="M950 338 Q958 368 992 356"/>
    <g role="img" aria-label="Map of Myanmar with national borders, EEZ in green, dotted state and region borders, and two marine corridors in blue and light red">
      <rect x="968" y="30" width="180" height="300" rx="6" fill="url(#map-tone)"/>
    </g>
  </g>
  <path class="flow-arrow" d="M1160 350 Q1185 420 1170 488" marker-end="url(#head-grey)"/>

  <g class="adaptive-management">
    <path class="flow-arrow" d="M812 338 Q870 292 928 272" marker-start="url(#head-grey)" marker-end="url(#head-grey)"/>
    <path class="flow-arrow" d="M822 396 Q890 382 955 348" marker-start="url(#head-grey)" marker-end="url(#head-grey)"/>
    <text class="adaptive-text" transform="translate(852 356) rotate(-22)">
      <tspan x="0" y="0">Adaptive</tspan>
      <tspan x="-6" y="21">management</tspan>
    </text>
  </g>

  <g class="national-benefits">
    <circle class="venn-economic" cx="1072" cy="528" r="72"/>
    <circle class="venn-social" cx="1000" cy="648" r="80"/>
    <circle class="venn-environment" cx="1150" cy="645" r="88"/>
    <g clip-path="url(#clip-econ)">
      <circle class="venn-econ-social" cx="1000" cy="648" r="80"/>
      <circle class="venn-econ-env" cx="1150" cy="645" r="88"/>
    </g>
    <g clip-path="url(#clip-social)">
      <circle class="venn-social-env" cx="1150" cy="645" r="88"/>
      <g clip-path="url(#clip-econ)">
        <circle class="venn-centre" cx="1150" cy="645" r="88"/>
      </g>
    </g>
    <text class="venn-label" x="1072" y="510">Economic</text>
    <text class="venn-label" x="1072" y="536">value</text>
    <text class="venn-label" x="988" y="626">Social</text>
    <text class="venn-label" x="988" y="652">development</text>
    <text class="venn-label" x="1162" y="626">Environmental</text>
    <text class="venn-label" x="1162" y="652">sustainability</text>
    <text class="benefits-script" transform="translate(886 716) rotate(-58)" textLength="320" lengthAdjust="spacingAndGlyphs">National Benefits</text>
  </g>
</svg>
</body>
</html>
```